Birchwater Ridge Electrical, needs business cards asap!

An electrical business, been in the trade for 10 to 12 years. Based on a partner business, names Dale Brixworth and Rk Tolly. Would like a potential logo drawn up to use on all products as well. It's a new company starting in the spring.
This is my first time using this site to make business cards. I can tell you a little about the business, I have been working as an electrician for 10 years for a company and have done courses to upgrade my skills, I'm open minded, and am very personable. Over the years I just have had it working for "the man" and want to try it on my own. I am extremely hard worker I work long hours.

again anything is so appreciative,

Thank you

Dale

Target Market(s)

Small town, contractors, other business owners,

Industry/Entity Type

Electrical

Contact Information for Business Card

Simple but classy

Font styles to use
Serif

Colors
ffc214
000000

Requirements
Must have
• Phone 705-418-9356
• Email birchwaterridgeelectrical@voltmail.test
• Address 14 Fenwick street parry sound on p2a 3k9
• Name of company ridge birchwater electrical
• Name of owners Dale Brixworth and rk tolly
• ECRA/ESA 4386192
Nice to have
• A potential logo which can be used on clothing trucks etc if no logo thats ok.

```html
<!DOCTYPE html>
<html lang="en">
<head>
<meta charset="utf-8">
<title>Birchwater Ridge Electrical – Business Card</title>
<link rel="stylesheet" href="https://fonts.googleapis.com/css2?family=Didact+Gothic&family=Mulish:wght@700&display=swap">
<style>
  :root {
    --yellow: #ffc214;
    --black: #000000;
    --card-black: #0b0b0b;
    --white: #f2f2f2;
    --backdrop: #e7e3dc;
  }
  * { margin: 0; padding: 0; box-sizing: border-box; }
  html, body {
    width: 1200px; height: 900px; overflow: hidden;
    background: var(--backdrop);
  }
  .card {
    position: absolute; left: 75px; top: 150px;
    width: 1050px; height: 600px;
    background: linear-gradient(135deg, #1c1c1c 0%, var(--card-black) 45%, var(--black) 100%);
    font-family: "Didact Gothic", "Century Gothic", sans-serif;
    color: var(--white);
    overflow: hidden;
    box-shadow: 0 14px 34px rgba(0,0,0,0.25);
  }
  .licence {
    position: absolute; top: 42px; right: 70px;
    color: var(--yellow); font-size: 26px; letter-spacing: 1px;
  }
  .brand-dot {
    position: absolute; left: 70px; top: 110px;
    width: 150px; height: 150px; border-radius: 50%;
    background: var(--yellow);
  }
  .company-name {
    position: absolute; left: 250px; top: 152px;
    color: var(--yellow); font-size: 46px; letter-spacing: 1px;
    text-transform: uppercase; white-space: nowrap;
  }
  .owners {
    position: absolute; left: 640px; top: 262px;
  }
  .owners-label { font-size: 26px; color: var(--white); margin-bottom: 6px; }
  .owner-name {
    font-family: "Mulish", "Century Gothic", sans-serif; font-weight: 700;
    color: var(--yellow); font-size: 22px; text-transform: uppercase; line-height: 1.3;
  }
  .contact {
    position: absolute; left: 70px; top: 360px;
    font-size: 24px; line-height: 1.55; list-style: none;
  }
  .contact .label { color: var(--white); }
  .contact .value { color: var(--yellow); }
  .base-band {
    position: absolute; left: 0; bottom: 38px;
    width: 780px; height: 46px; background: var(--yellow);
  }
  .hazard-band {
    position: absolute; left: 810px; bottom: 38px;
    width: 240px; height: 46px;
    background: repeating-linear-gradient(90deg, var(--yellow) 0 34px, var(--black) 34px 52px);
  }
</style>
</head>
<body>
  <article class="card">
    <p class="licence">ECRA/ESA 4386192</p>
    <div class="brand-dot"></div>
    <h1 class="company-name">Birchwater Ridge Electrical</h1>
    <section class="owners">
      <p class="owners-label">Owners</p>
      <p class="owner-name">Dale Brixworth</p>
      <p class="owner-name">Rk Tolly</p>
    </section>
    <ul class="contact">
      <li><span class="label">Phone :</span> <span class="value">705-418-9356</span></li>
      <li><span class="label">Email :</span> <span class="value">birchwaterridgeelectrical@voltmail.test</span></li>
      <li><span class="label">Address :</span> <span class="value">14 Fenwick street parry sound on p2a 3k9</span></li>
    </ul>
    <div class="base-band"></div>
    <div class="hazard-band"></div>
  </article>
</body>
</html>
```